Certificate of Completion - Educational Trainings

We are looking for a certificate of completion for individuals who complete one of our specific trainings. Files should be provided in a Word (docx) or PowerPoint (pptx) format. The "Halvorcrest example.png" file is to show necessary information. Copies of logos have been included for design purposes.

Target Market(s)

Training Participants

Industry/Entity Type

Healthcare

Font styles to use
Sans Serif

```html
<!DOCTYPE html>
<html lang="en">
<head>
<meta charset="utf-8">
<title>Halvorcrest Certificate of Completion</title>
<link rel="stylesheet" href="https://fonts.googleapis.com/css2?family=Bebas+Neue&family=Pathway+Gothic+One&family=Great+Vibes&display=swap">
<style>
  :root {
    --page-bg: #f1f2f4;
    --paper: #ffffff;
    --green-dark: #156b37;
    --green-light: #6ab04c;
    --ink: #111111;
    --white: #ffffff;
  }
  * { margin: 0; padding: 0; box-sizing: border-box; }
  html, body {
    width: 1200px; height: 1000px; overflow: hidden;
    background: var(--page-bg);
  }
  .certificate {
    position: absolute; left: 294px; top: 105px;
    width: 611px; height: 791px;
    background: var(--paper);
    box-shadow: 0 8px 22px rgba(0,0,0,0.22);
    font-family: "Pathway Gothic One", sans-serif;
    color: var(--ink);
    text-align: center;
    overflow: hidden;
  }
  .frame { position: absolute; left: 0; top: 0; }
  .brand {
    position: absolute; left: 0; right: 0; top: 48px;
    display: flex; flex-direction: column; align-items: center;
  }
  .brand-dot {
    width: 44px; height: 44px; border-radius: 50%;
    background: var(--green-dark);
  }
  .brand-name {
    margin-top: 24px;
    font-size: 32px; letter-spacing: 4px; line-height: 1;
    color: var(--ink);
  }
  .sponsor-info {
    position: absolute; left: 0; right: 0; top: 156px;
    font-size: 18px; line-height: 19.5px;
  }
  .title-band {
    position: absolute; left: 0; right: 0; top: 250px; height: 91px;
  }
  .band-block {
    position: absolute; top: 0; width: 50px; height: 91px;
    background: var(--green-dark);
  }
  .band-block.left { left: 0; }
  .band-block.right { right: 0; }
  .title {
    position: absolute; left: 0; right: 0; top: -16px;
    font-family: "Bebas Neue", sans-serif;
    font-size: 132px; line-height: 1;
    color: var(--green-dark);
    letter-spacing: -1px;
  }
  .subtitle {
    position: absolute; left: 0; right: 0; top: 338px;
    font-family: "Great Vibes", cursive;
    font-size: 52px; line-height: 1;
    color: var(--green-light);
  }
  .awarded-to {
    position: absolute; left: 0; right: 0; top: 396px;
    font-size: 46px; line-height: 1;
  }
  .recipient {
    position: absolute; left: 0; right: 0; top: 462px;
    font-family: "Great Vibes", cursive;
    font-size: 62px; line-height: 1;
    color: var(--green-dark);
  }
  .recipient-rule {
    position: absolute; left: 87px; width: 446px; top: 529px;
    height: 1.5px; background: var(--green-dark);
  }
  .course-details {
    position: absolute; left: 0; right: 0; top: 550px;
    font-size: 31px; line-height: 28.5px;
  }
  .completion {
    position: absolute; right: 113px; top: 686px;
    text-align: right;
  }
  .completion-date { font-size: 12px; }
  .completion-date strong { font-weight: 400; font-size: 19px; }
  .signer-name {
    margin-top: 6px;
    font-family: "Bebas Neue", sans-serif;
    font-size: 18px; line-height: 1;
    text-decoration: underline; text-underline-offset: 2px;
  }
  .signer-role { font-size: 12px; margin-top: 2px; }
  .footer-band {
    position: absolute; left: 0; right: 0; bottom: 0; height: 29px;
    background: var(--green-light);
    color: var(--white);
    font-size: 12px; line-height: 29px;
  }
</style>
</head>
<body>
  <main class="certificate">
    <svg class="frame" width="611" height="791" viewBox="0 0 611 791" aria-hidden="true">
      <path d="M13 250 V38 L38 26 L40 12 H571 L573 26 L598 38 V250" fill="none" stroke="var(--green-light)" stroke-width="2"/>
      <path d="M13 341 V762 M598 341 V762" fill="none" stroke="var(--green-light)" stroke-width="2"/>
    </svg>

    <header class="brand">
      <span class="brand-dot"></span>
      <span class="brand-name">HALVORCREST</span>
    </header>

    <p class="sponsor-info">
      48 HARBOR ROAD, STE. 310<br>
      EASTBROOK, ME 04210<br>
      UNIFIED REGISTRY SPONSOR NUMBER 70318
    </p>

    <section class="title-band">
      <span class="band-block left"></span>
      <h1 class="title">CERTIFICATE</h1>
      <span class="band-block right"></span>
    </section>

    <p class="subtitle">of completion</p>
    <p class="awarded-to">THIS CERTIFICATE IS AWARDED TO</p>
    <p class="recipient">Marcus Ellinwood</p>
    <div class="recipient-rule"></div>

    <p class="course-details">
      FOR SUCCESSFUL COMPLETION OF<br>
      BEST PRACTICES: BUDGET PROCESS/BUDGET BUILDING<br>
      COMPLETED ONLINE FIELD OF STUDY FINANCE<br>
      CPE CREDITS: 1
    </p>

    <div class="completion">
      <p class="completion-date">COMPLETION DATE : <strong>05/16/2024</strong></p>
      <p class="signer-name">CLARA VENSE</p>
      <p class="signer-role">SENIOR CONSULTANT</p>
    </div>

    <footer class="footer-band">
      IN ACCORDANCE WITH THE STANDARD OF THE UNIFIED REGISTRY OF CPE SPONSORS, CPE CREDITS HAVE BEEN GRANTED BASED ON A 50 MINUTE HOUR.
    </footer>
  </main>
</body>
</html>
```